Web Site Design

Lumen Ledgerworks has developed a cloud based accounting systems for small businesses that have out grown products like TallyNest. We are in the process of launching our web site at www.try-lumenly.com. It is hosted on www.pagecradle.com.

Tag Lines:
Simply Innovative Business Management

Cloud Accounting-Anywhere, Anytime, Anyplace

Target Market(s)

Small to med businesses.

Industry/Entity Type

Accounting

Coding

Coded - Design and coding required

Number of Pages Required

5+ page

Font styles to use
Other font styles liked:
• Futura

Requirements
Must have
• I have uploaded graphic pages from a brochure that is being developed.
• I would like to follow the same theme.
• Pages:
• Home Page - Attractive, place holder for ClipHarbor video
• Product Page - Description
• Industries - Discussion of key industries
• Contact
• About

```html
<!DOCTYPE html>
<html lang="en">
<head>
<meta charset="utf-8">
<title>Lumen Ledgerworks — Accounting and Business Management Software</title>
<link href="https://fonts.googleapis.com/css2?family=Jost:wght@300;400;500;600&family=Open+Sans:wght@400;600&display=swap" rel="stylesheet">
<style>
  :root {
    --brand-red: #c8141b;
    --brand-red-dark: #a90f15;
    --ink: #333333;
    --ink-soft: #6b6b6b;
    --paper: #ffffff;
    --footer: #3a3a3a;
    --footer-text: #d8d8d8;
    --overlay: rgba(40, 40, 40, 0.78);
  }
  * { box-sizing: border-box; margin: 0; padding: 0; }
  html, body { width: 859px; height: 1200px; overflow: hidden; background: var(--paper); }
  body { font-family: "Open Sans", Arial, sans-serif; color: var(--ink); position: relative; }

  .site-header { height: 70px; display: flex; align-items: center; justify-content: space-between; padding: 0 48px 0 96px; }
  .brand { display: flex; align-items: center; gap: 8px; }
  .brand-dot { width: 30px; height: 30px; border-radius: 50%; background: var(--brand-red); }
  .brand-name { font-family: "Jost", sans-serif; font-weight: 600; font-size: 17px; color: var(--brand-red); letter-spacing: 0.5px; text-transform: uppercase; line-height: 1; }
  .main-nav { display: flex; gap: 34px; }
  .main-nav a { font-family: "Jost", sans-serif; font-size: 13px; color: var(--ink); text-decoration: none; }

  .hero { position: relative; height: 370px; }
  .hero-photo { position: absolute; inset: 0; background: linear-gradient(120deg, #d9dcdf 0%, #aeb3b8 35%, #8e949a 60%, #c7cbcf 100%); }
  .hero-panel { position: absolute; left: 270px; top: 90px; width: 320px; background: var(--overlay); color: #fff; text-align: center; padding: 18px 20px 16px; }
  .hero-title { font-family: "Jost", sans-serif; font-weight: 500; font-size: 22px; line-height: 1.15; text-transform: uppercase; white-space: nowrap; }
  .hero-text { font-size: 8px; line-height: 1.5; margin-top: 8px; color: #e4e4e4; }
  .hero-dots { position: absolute; left: 0; right: 0; top: 310px; display: flex; justify-content: center; gap: 6px; }
  .hero-dots span { width: 7px; height: 7px; border-radius: 50%; background: rgba(255,255,255,0.6); }
  .hero-dots span:first-child { background: #fff; }

  .intro { text-align: center; padding: 24px 96px 0; }
  .intro-title { font-family: "Jost", sans-serif; font-weight: 400; font-size: 27px; color: var(--ink); }
  .intro .intro-sub { font-family: "Jost", sans-serif; font-weight: 300; font-size: 20px; margin-top: 0; text-align: center; color: var(--ink); line-height: 1.3; }
  .intro .intro-copy { font-size: 8.5px; line-height: 1.6; color: var(--ink-soft); margin-top: 9px; text-align: left; }

  .features { position: absolute; top: 650px; left: 0; width: 859px; height: 272px; background: var(--brand-red); color: #fff; text-align: center; }
  .features-title { font-family: "Jost", sans-serif; font-weight: 400; font-size: 22px; margin-top: 28px; }
  .features-rule { width: 250px; height: 1px; background: rgba(255,255,255,0.5); margin: 8px auto 0; }
  .feature-list { display: flex; justify-content: center; gap: 26px; margin-top: 18px; }
  .feature { width: 160px; }
  .feature-icon { width: 58px; height: 58px; border-radius: 50%; background: var(--brand-red-dark); border: 2px solid #fff; margin: 0 auto; display: flex; align-items: center; justify-content: center; }
  .feature-name { font-family: "Jost", sans-serif; font-weight: 500; font-size: 12px; line-height: 1.25; margin-top: 10px; }
  .feature-text { font-size: 7.5px; line-height: 1.5; margin-top: 5px; color: #f6dada; }

  .vision { position: absolute; top: 945px; left: 96px; width: 720px; display: flex; justify-content: space-between; }
  .vision-copy { width: 395px; }
  .vision-title { font-family: "Jost", sans-serif; font-weight: 500; font-size: 16px; text-transform: uppercase; }
  .vision-copy p { font-size: 8px; line-height: 1.55; color: var(--ink-soft); margin-top: 8px; }
  .read-more { display: inline-block; margin-top: 12px; padding: 5px 12px; border: 1px solid #999; font-size: 8px; color: var(--ink); text-transform: uppercase; text-decoration: none; }
  .video-slot { width: 300px; height: 130px; margin-top: 12px; background: linear-gradient(135deg, #cfd4da, #8f98a2); position: relative; }
  .play { position: absolute; left: 50%; top: 50%; transform: translate(-50%, -50%); }

  .site-footer { position: absolute; top: 1120px; left: 0; width: 859px; height: 80px; background: var(--footer); color: var(--footer-text); padding: 16px 96px; }
  .footer-row { display: flex; justify-content: space-between; align-items: center; }
  .footer-nav { display: flex; gap: 14px; font-size: 9px; }
  .footer-nav a { color: var(--footer-text); text-decoration: none; }
  .social { display: flex; gap: 8px; }
  .social span { width: 14px; height: 14px; border-radius: 50%; background: #8a8a8a; }
  .copyright { font-size: 8px; margin-top: 8px; color: #a9a9a9; }
</style>
</head>
<body>
  <header class="site-header">
    <div class="brand"><span class="brand-dot"></span><span class="brand-name">Lumen Ledgerworks</span></div>
    <nav class="main-nav"><a href="#">About Us</a><a href="#">Products</a><a href="#">Features</a><a href="#">Contact</a></nav>
  </header>

  <section class="hero">
    <div class="hero-photo" role="img" aria-label="Office team working together at a desk"></div>
    <div class="hero-panel">
      <h1 class="hero-title">Simply Innovative<br>Business Management</h1>
      <p class="hero-text">Cloud accounting anywhere, anytime, anyplace. Run your books, sales and service from one browser.</p>
    </div>
    <div class="hero-dots"><span></span><span></span><span></span><span></span></div>
  </section>

  <section class="intro">
    <h2 class="intro-title">Accounting and Business Management Software</h2>
    <div class="intro-sub">Online business management</div>
    <p class="intro-copy">Lumen Ledgerworks is the first cloud business management platform built for growing small and mid-sized companies. It combines accounting, inventory, sales and customer service in a single system so your team can work from one set of records, wherever they are.</p>
    <p class="intro-copy">When basic bookkeeping tools like TallyNest no longer keep pace, our software grows with you. Add users, locations and modules as you need them, and keep every report current without manual exports or duplicate data entry.</p>
    <p class="intro-copy">Secure hosting, automatic backups and regular updates are included, so you can focus on running your business instead of maintaining servers.</p>
  </section>

  <section class="features">
    <h2 class="features-title">Product Features</h2>
    <div class="features-rule"></div>
    <div class="feature-list">
      <div class="feature">
        <div class="feature-icon"><svg width="26" height="26" viewBox="0 0 26 26" fill="none" stroke="#fff" stroke-width="2"><rect x="3" y="5" width="20" height="16" rx="1"/><line x1="3" y1="10" x2="23" y2="10"/></svg></div>
        <p class="feature-name">Built on the Orbitra<br>CRM Platform</p>
        <p class="feature-text">Sales, service and accounting share one familiar platform your staff already understands.</p>
      </div>
      <div class="feature">
        <div class="feature-icon"><svg width="26" height="26" viewBox="0 0 26 26" fill="none" stroke="#fff" stroke-width="2.5"><polyline points="5,13 11,19 21,7"/></svg></div>
        <p class="feature-name">Full Audit Trail</p>
        <p class="feature-text">Every change is recorded with date, time and user so your records always stay accountable.</p>
      </div>
      <div class="feature">
        <div class="feature-icon"><svg width="26" height="26" viewBox="0 0 26 26" fill="none" stroke="#fff" stroke-width="2"><path d="M20 13a7 7 0 1 1-3-5.7"/><polyline points="17,3 17,8 22,8"/></svg></div>
        <p class="feature-name">One Button<br>Correction</p>
        <p class="feature-text">Fix a posted entry in a single step, with the reversing journal created for you.</p>
      </div>
      <div class="feature">
        <div class="feature-icon"><svg width="28" height="22" viewBox="0 0 28 22" fill="none" stroke="#fff" stroke-width="2"><path d="M7 18h14a5 5 0 0 0 0-10 7 7 0 0 0-13-1A5 5 0 0 0 7 18z"/></svg></div>
        <p class="feature-name">Cloud-Based, Browser<br>Independent</p>
        <p class="feature-text">Work from any device and any modern browser, with nothing to install or update.</p>
      </div>
    </div>
  </section>

  <section class="vision">
    <div class="vision-copy">
      <h2 class="vision-title">Our Vision &amp; Services</h2>
      <p>We believe growing businesses deserve the same tools as large enterprises, without the cost or complexity. Our team helps you move from spreadsheets and entry-level software to one connected system.</p>
      <p>From data migration and setup to training and ongoing support, we stay with you at every step so your new platform works from the very first day.</p>
      <a class="read-more" href="#">Read More</a>
    </div>
    <div class="video-slot" role="img" aria-label="ClipHarbor video placeholder showing the product overview">
      <svg class="play" width="40" height="40" viewBox="0 0 40 40"><circle cx="20" cy="20" r="19" fill="rgba(0,0,0,0.45)"/><polygon points="16,12 29,20 16,28" fill="#fff"/></svg>
    </div>
  </section>

  <footer class="site-footer">
    <div class="footer-row">
      <nav class="footer-nav"><a href="#">About</a><span>|</span><a href="#">Products</a><span>|</span><a href="#">Features</a><span>|</span><a href="#">Support</a><span>|</span><a href="#">Contact</a></nav>
      <div class="social"><span></span><span></span><span></span><span></span></div>
    </div>
    <p class="copyright">© 2015 Lumen Ledgerworks. All rights reserved. www.try-lumenly.com</p>
  </footer>
</body>
</html>
```